willow crest business card project

Financial consulting in line with life insurance ,index annuity, college funding solutions. I educate clients on cash flow, debt management, how to create emergency fund, how to proper protection with the best insurance, how to accummulate asset and management, how to preserve asset/ estate planning. Collge funding solutions help familes seek the best funding solutions possible including award letter review and test prep on QEV, BRM, LBRM, BRM II
Target Market(s)
Individuals, family, business
Industry/Entity Type
Financial Planning
Contact Information for Business Card
Business name: Willow Crest Financial Services
Dorin Velko
Managing Director
License no. 5K32416
Address: 2193 Thistlebrook Ave. Baldwin Park, CA 91724
Phone: 714-555-0193 Fax: 626-555-0147
Email: dorin.velko@mailbrook.example
Other font styles liked:
- Bliss
Requirements
Must have
- Use feng shui as a guide to design the card make a flow curve lines only no angle or arrows.Size 3.5 inch by 2inch, metallic look is good, design a logo too . Keep it simple add image using feng shuis a guide. Also put a tagline that can make a very good impression. Use the back with something that the client we be able to use feng shui as guide.
Nice to have
- Use feng shui as guiding principle. Keep it simple
- Logo and tagline
Should not have
- Negative chi ,Angles, down ward design, too many things or too many images

```html
<!DOCTYPE html>
<html lang="en">
<head>
<meta charset="utf-8">
<title>Willow Crest Financial Services – Business Card</title>
<link rel="stylesheet" href="https://fonts.googleapis.com/css2?family=Source+Sans+3:wght@300;400;600&display=swap">
<style>
  :root {
    --backdrop: #000000;
    --card-top: #38393b;
    --card-bottom: #313234;
    --ink: #e6e6e6;
    --ink-soft: #c9c9c9;
    --rule: #4a4b4d;
  }
  * { margin: 0; padding: 0; box-sizing: border-box; }
  html, body {
    width: 1200px; height: 900px; overflow: hidden;
    background: var(--backdrop);
    font-family: "Source Sans 3", "Helvetica Neue", Arial, sans-serif;
    color: var(--ink);
  }
  .stage { position: relative; width: 1200px; height: 900px; }
  .card {
    position: absolute; top: 271px;
    width: 456px; height: 281px;
    border-radius: 12px;
    background: linear-gradient(180deg, var(--card-top), var(--card-bottom));
  }
  .card--front { left: 137px; }
  .card--back { left: 627px; }

  .brand-mark {
    position: absolute; left: 20px; top: 90px; width: 202px;
    text-align: center;
  }
  .brand-mark__dot {
    display: block; margin: 0 auto 10px;
    width: 26px; height: 26px; border-radius: 50%;
    border: 2px solid var(--ink-soft);
  }
  .brand-mark__name { font-size: 24px; font-weight: 300; letter-spacing: 0.5px; color: var(--ink); }

  .divider {
    position: absolute; left: 218px; top: 80px;
    width: 1px; height: 116px; background: var(--rule);
  }
  .contact { position: absolute; left: 254px; top: 58px; }
  .contact__name { font-size: 17px; font-weight: 600; line-height: 20px; }
  .contact__role { font-size: 12.5px; line-height: 16px; color: var(--ink-soft); }
  .contact__address { margin-top: 20px; font-size: 12.5px; line-height: 18px; color: var(--ink-soft); }
  .contact__lines { margin-top: 18px; list-style: none; font-size: 12.5px; line-height: 19px; color: var(--ink-soft); }
  .contact__lines li { display: flex; align-items: center; }
  .contact__lines svg { width: 9px; height: 9px; margin-right: 10px; fill: var(--ink-soft); flex: none; }

  .wordmark {
    position: absolute; left: 0; right: 0; top: 112px;
    text-align: center;
  }
  .wordmark__line { display: flex; align-items: center; justify-content: center; gap: 12px; }
  .wordmark__name { font-size: 42px; font-weight: 300; line-height: 42px; color: var(--ink); }
  .wordmark__dot { width: 16px; height: 16px; border-radius: 50%; border: 2px solid var(--ink); }
  .wordmark__tag { margin-top: 2px; font-size: 13px; font-weight: 300; letter-spacing: 0.6px; color: var(--ink-soft); }
</style>
</head>
<body>
<main class="stage">
  <section class="card card--front" aria-label="Card front">
    <div class="brand-mark">
      <span class="brand-mark__dot"></span>
      <span class="brand-mark__name">Willow Crest</span>
    </div>
    <div class="divider"></div>
    <div class="contact">
      <p class="contact__name">Dorin Velko</p>
      <p class="contact__role">Managing Director</p>
      <p class="contact__address">2193 Thistlebrook Ave.<br>Baldwin Park, CA 91724</p>
      <ul class="contact__lines">
        <li><svg viewBox="0 0 10 10" aria-hidden="true"><path d="M2 0.5 L3.6 2.6 L2.8 3.6 C3.4 5 4.8 6.4 6.3 7.1 L7.3 6.3 L9.5 7.9 L8.6 9.5 C4.5 9.2 0.8 5.5 0.5 1.4 Z"/></svg>714-555-0193</li>
        <li><svg viewBox="0 0 10 10" aria-hidden="true"><path d="M2.5 0.5 H7 V3 H2.5 Z M0.5 3.5 H9.5 V9.5 H0.5 Z M2 5 V6 H3 V5 Z M4.5 5 V6 H5.5 V5 Z M7 5 V6 H8 V5 Z M2 7 V8 H3 V7 Z M4.5 7 V8 H5.5 V7 Z M7 7 V8 H8 V7 Z"/></svg>626-555-0147</li>
        <li><svg viewBox="0 0 10 10" aria-hidden="true"><path d="M0.5 2 H9.5 V8.5 H0.5 Z M1.2 2.6 L5 5.6 L8.8 2.6 V3.6 L5 6.6 L1.2 3.6 Z" fill-rule="evenodd"/></svg>dorin.velko@mailbrook.example</li>
      </ul>
    </div>
  </section>

  <section class="card card--back" aria-label="Card back">
    <div class="wordmark">
      <div class="wordmark__line">
        <span class="wordmark__name">Willow Crest</span>
        <span class="wordmark__dot"></span>
      </div>
      <p class="wordmark__tag">FINANCIAL SERVICES</p>
    </div>
  </section>
</main>
</body>
</html>
```